Cold brew coffee concept

Web site/logo for cold brew coffee served in a keg tap. Cold brew coffee is a natural energy beverage roasted with fair trade/organic beans. Based in New England. Think- Fresh, Natural, Organic, Pure, Mills, Brick, Wood. Ferncastle Coldbrew.

Target Market(s)

Individuals looking for energy drinks without added sugar or dairy. Coffee connoisseurs.

Industry/Entity Type

Trade

Logo Text

Ferncastle Coldbrew

Number of Pages Required

1 page

Font styles to use
Serif

```html
<!DOCTYPE html>
<html lang="en">
<head>
<meta charset="utf-8">
<title>Ferncastle Coldbrew — Cold Brew Coffee</title>
<link rel="stylesheet" href="https://fonts.googleapis.com/css2?family=Montserrat:wght@300;400;600;700&family=Open+Sans:wght@400;600&display=swap">
<style>
:root{
  --green:#3f8a35;
  --green-dark:#2f6e27;
  --green-soft:#5a9a4c;
  --brown:#4a2c1b;
  --ink:#3b3b3b;
  --muted:#666;
  --light:#ececec;
  --white:#fff;
  --line:#e3e3e3;
}
*{box-sizing:border-box;margin:0;padding:0}
html,body{width:1200px;height:3051px;overflow:hidden;background:var(--white)}
body{font-family:"Open Sans",Arial,sans-serif;color:var(--ink);position:relative}
.heading{font-family:"Montserrat",Arial,sans-serif}

/* Header */
.site-header{position:absolute;top:0;left:0;width:1200px;height:148px;background:var(--white);z-index:5}
.brand{position:absolute;left:102px;top:-10px;width:224px;height:224px;border-radius:50%;background:var(--green);border:8px solid var(--white);box-shadow:0 3px 8px rgba(0,0,0,.25);display:flex;flex-direction:column;align-items:center;justify-content:center;z-index:6}
.brand-name{font-family:"Montserrat",Arial,sans-serif;font-weight:700;color:var(--white);font-size:23px;line-height:1.25;text-align:center;letter-spacing:.5px}
.cart{position:absolute;left:638px;top:22px;width:176px;height:36px;border:1px solid var(--line);display:flex;align-items:center;padding-left:14px;font-family:"Montserrat",Arial,sans-serif;font-size:11px;font-weight:600;color:#222;gap:10px}
.cart .caret{position:absolute;right:12px;top:12px}
.search{position:absolute;left:840px;top:22px;width:260px;height:36px;border:1px solid var(--line);font-size:11px;color:#999;padding:10px 16px;position:absolute}
.search svg{position:absolute;right:14px;top:11px}
.main-nav{position:absolute;left:414px;top:90px;display:flex;gap:0}
.main-nav a{font-family:"Montserrat",Arial,sans-serif;font-size:13px;font-weight:600;color:#222;text-decoration:none;margin-right:48px}
.main-nav a.active{color:#7a5a2b}
.main-nav a:last-child{margin-right:0}

/* Hero */
.hero{position:absolute;top:148px;left:0;width:1200px;height:523px;overflow:hidden}
.hero-photo{position:absolute;inset:0;background:radial-gradient(ellipse at 50% 55%,#b9c6a4 0%,#8fb07a 35%,#5f9a4e 70%,#4c8c40 100%)}
.hero-title{position:absolute;top:180px;width:100%;text-align:center;font-family:"Montserrat",Arial,sans-serif;font-weight:700;font-size:76px;color:var(--white);letter-spacing:1px;line-height:1}
.hero-sub{position:absolute;top:265px;width:100%;text-align:center;font-family:"Montserrat",Arial,sans-serif;font-size:29px;color:var(--white)}
.hero-dots{position:absolute;top:446px;left:564px;display:flex;gap:3px}
.hero-dots span{width:16px;height:16px;border-radius:50%;background:var(--white);border:2px solid var(--white)}
.hero-dots span.off{background:transparent}
.hero-curve{position:absolute;left:0;bottom:0}

/* Welcome */
.welcome{position:absolute;top:671px;left:0;width:1200px;text-align:center}
.welcome h2{margin-top:36px;font-size:30px;font-weight:700;color:var(--brown);letter-spacing:.5px}
.welcome h2 em{font-style:normal;color:var(--green)}
.welcome p{width:850px;margin:26px auto 0;font-size:13px;line-height:27px;color:var(--muted)}
.welcome hr{width:1000px;margin:36px auto 0;border:0;border-top:1px solid var(--line)}

.products{position:absolute;top:913px;left:98px;display:flex;gap:22px}
.product-card{width:236px;height:364px;border:1px solid var(--line);padding:10px 10px 0}
.product-photo{width:214px;height:155px}
.product-card h3{font-family:"Montserrat",Arial,sans-serif;font-size:17px;font-weight:700;color:#111;margin-top:24px}
.product-card p{font-size:12.5px;line-height:21px;color:var(--muted);margin-top:4px}
.product-actions{display:flex;justify-content:space-between;margin-top:28px}
.btn-small{height:29px;padding:0 12px;display:flex;align-items:center;gap:5px;font-size:11.5px;font-weight:600;color:var(--white);border-radius:2px}
.btn-shop{background:var(--green)}
.btn-cart{background:var(--brown)}

/* Brew band */
.brew{position:absolute;top:1345px;left:0;width:1200px;height:441px;color:var(--white);text-align:center}
.brew-photo{position:absolute;inset:0;background:linear-gradient(180deg,#4a8e3f 0%,#55964a 55%,#3f8535 100%)}
.brew-inner{position:relative;padding-top:52px}
.brew h2{font-size:48px;font-weight:300;letter-spacing:1px}
.brew p{width:900px;margin:26px auto 0;font-size:14px;line-height:26px}
.brew p + p{width:760px;margin-top:18px}

/* Our products */
.about{position:absolute;top:1786px;left:0;width:1200px;height:421px;text-align:center}
.about-photo{position:absolute;inset:0;background:linear-gradient(90deg,#f0f0f0 0%,#e8e8e8 60%,#dcdcdc 100%)}
.about-inner{position:relative;padding-top:44px}
.about h2{font-size:33px;font-weight:700;color:var(--brown)}
.about h2 em{font-style:normal;color:var(--green)}
.about p{width:900px;margin:24px auto 0;font-size:17px;line-height:26px;color:#333}
.about p + p{margin-top:22px}
.btn-more{display:inline-flex;align-items:center;gap:12px;height:53px;padding:0 36px;font-family:"Montserrat",Arial,sans-serif;font-size:17px;color:var(--white)}
.about .btn-more{background:var(--green);margin-top:30px;width:216px;justify-content:center}

/* History */
.history{position:absolute;top:2207px;left:0;width:1200px;height:529px;color:var(--white);text-align:center}
.history-photo{position:absolute;inset:0;background:radial-gradient(ellipse at 45% 45%,#6ba55e 0%,#4d913f 55%,#418838 100%)}
.history-inner{position:relative;padding-top:128px}
.history h2{font-size:34px;font-weight:700;letter-spacing:.5px}
.history .lead{font-family:"Montserrat",Arial,sans-serif;font-size:25px;margin-top:22px}
.history p.body{width:900px;margin:18px auto 0;font-size:17px;line-height:27px}
.history .btn-more{border:2px solid var(--white);margin-top:44px;width:220px;justify-content:center}

/* Footer */
.site-footer{position:absolute;top:2736px;left:0;width:1200px;height:315px;background:var(--green);color:var(--white)}
.footer-col{position:absolute;top:40px}
.footer-col h4{font-family:"Montserrat",Arial,sans-serif;font-size:19px;font-weight:400;letter-spacing:.5px}
.col-contact{left:100px}
.col-contact p{font-size:12.5px;line-height:30px;margin-top:6px}
.col-contact p:first-of-type{margin-top:14px}
.col-contact p{margin-top:0}
.col-touch{left:494px}
.col-follow{left:925px}
.col-follow p{font-size:12.5px;margin-top:18px}
.divider-v{position:absolute;top:30px;width:1px;height:225px;background:rgba(255,255,255,.2)}
.contact-form{margin-top:14px;width:352px}
.field{background:var(--white);height:28px;font-size:12px;color:#aaa;padding:5px 12px}
.field-row{display:flex;gap:12px}
.field-row .field{width:170px}
.field-area{height:54px;margin-top:12px}
.btn-send{margin-top:22px;width:136px;height:36px;background:var(--brown);display:flex;align-items:center;justify-content:center;font-family:"Montserrat",Arial,sans-serif;font-size:16px;font-weight:600}
.social{display:flex;gap:6px;margin-top:14px}
.social span{width:36px;height:36px;border-radius:50%;border:2px solid var(--white)}
.social .s1{background:#3aa3de}.social .s2{background:#2f5aa3}.social .s3{background:#1f7bb6}.social .s4{background:#d9473a}
.footer-bottom{position:absolute;top:250px;left:98px;width:1004px;border-top:1px solid rgba(255,255,255,.4);padding-top:20px;font-size:11.5px;display:flex;justify-content:space-between}
.footer-bottom .code{margin-right:-36px}
</style>
</head>
<body>

<header class="site-header">
  <div class="brand"><span class="brand-name">FERNCASTLE<br>COLDBREW</span></div>
  <div class="cart">
    <svg width="16" height="14" viewBox="0 0 16 14" aria-hidden="true"><path d="M0 1h3l2 8h8l2-6H4.5" fill="none" stroke="#222" stroke-width="1.6"/><circle cx="6" cy="12" r="1.4" fill="#222"/><circle cx="12" cy="12" r="1.4" fill="#222"/></svg>
    CART &nbsp;(EMPTY)
    <svg class="caret" width="10" height="8" viewBox="0 0 10 8" aria-hidden="true"><path d="M1 2l4 4 4-4" fill="none" stroke="#444" stroke-width="1.4"/></svg>
  </div>
  <div class="search">Search entire store here...
    <svg width="12" height="12" viewBox="0 0 12 12" aria-hidden="true"><circle cx="5" cy="5" r="3.8" fill="none" stroke="#888" stroke-width="1.4"/><path d="M8 8l3 3" stroke="#888" stroke-width="1.5"/></svg>
  </div>
  <nav class="main-nav">
    <a class="active" href="#">HOME</a><a href="#">ABOUT US</a><a href="#">PRODUCTS</a><a href="#">OUR STORE</a><a href="#">WHOLESALE</a><a href="#">CONTACT US</a>
  </nav>
</header>

<section class="hero">
  <div class="hero-photo" role="img" aria-label="Glass of iced cold brew coffee topped with mint on a blurred green lawn, green tinted"></div>
  <h1 class="hero-title">COLD BREW COFFEE</h1>
  <p class="hero-sub">We sell cold brew coffee served in a keg tap</p>
  <div class="hero-dots"><span class="off"></span><span></span><span></span><span></span></div>
  <svg class="hero-curve" width="1200" height="90" viewBox="0 0 1200 90" aria-hidden="true"><path d="M0 20 Q600 160 1200 20 V90 H0Z" fill="#fff"/></svg>
</section>

<section class="welcome">
  <h2 class="heading">WELCOME TO <em>FERNCASTLE COLDBREW</em></h2>
  <p>Sed ut perspiciatis unde omnis iste natus error sit voluptatem accusantium doloremque laudantium, totam rem aperiam, eaque ipsa quae ab illo inventore veritatis et quasi architecto beatae vitae dicta sunt explicabo. Nemo enim ipsam voluptatem quia voluptas sit aspernatur aut odit aut fugit, sed quia consequuntur magni dolores eos qui ratione voluptatem sequi nesciunt.</p>
  <hr>
</section>

<div class="products">
  <article class="product-card">
    <div class="product-photo" role="img" aria-label="Glass of black coffee surrounded by roasted coffee beans" style="background:linear-gradient(160deg,#e9e6e2 0%,#8a6a50 60%,#3a2316 100%)"></div>
    <h3>NATURAL ENERGY</h3>
    <p>Characterized by an extremely fine drink, strong body, excellent aroma and sweetness...</p>
    <div class="product-actions"><span class="btn-small btn-shop">Shop Now</span><span class="btn-small btn-cart"><svg width="11" height="10" viewBox="0 0 16 14" aria-hidden="true"><path d="M0 1h3l2 8h8l2-6H4.5Z" fill="#fff"/><circle cx="6" cy="12" r="1.6" fill="#fff"/><circle cx="12" cy="12" r="1.6" fill="#fff"/></svg>Add to Cart</span></div>
  </article>
  <article class="product-card">
    <div class="product-photo" role="img" aria-label="Chocolate pieces and coffee beans on a dark wooden surface" style="background:linear-gradient(160deg,#6b4230 0%,#4a2a1a 55%,#2c170d 100%)"></div>
    <h3>BEVERAGE ROASTED</h3>
    <p>Characterized by an extremely fine drink, strong body, excellent aroma and sweetness...</p>
    <div class="product-actions"><span class="btn-small btn-shop">Shop Now</span><span class="btn-small btn-cart"><svg width="11" height="10" viewBox="0 0 16 14" aria-hidden="true"><path d="M0 1h3l2 8h8l2-6H4.5Z" fill="#fff"/><circle cx="6" cy="12" r="1.6" fill="#fff"/><circle cx="12" cy="12" r="1.6" fill="#fff"/></svg>Add to Cart</span></div>
  </article>
  <article class="product-card">
    <div class="product-photo" role="img" aria-label="Iced coffee glass with beans and cups on a wooden table" style="background:linear-gradient(160deg,#c9b49a 0%,#9a7a5c 55%,#5c3e28 100%)"></div>
    <h3>FAIR TRADE</h3>
    <p>Characterized by an extremely fine drink, strong body, excellent aroma and sweetness...</p>
    <div class="product-actions"><span class="btn-small btn-shop">Shop Now</span><span class="btn-small btn-cart"><svg width="11" height="10" viewBox="0 0 16 14" aria-hidden="true"><path d="M0 1h3l2 8h8l2-6H4.5Z" fill="#fff"/><circle cx="6" cy="12" r="1.6" fill="#fff"/><circle cx="12" cy="12" r="1.6" fill="#fff"/></svg>Add to Cart</span></div>
  </article>
  <article class="product-card">
    <div class="product-photo" role="img" aria-label="Wooden coffee grinder filled with organic roasted beans" style="background:linear-gradient(160deg,#d8cfc4 0%,#7a4e30 50%,#3b2214 100%)"></div>
    <h3>ORGANIC BEANS</h3>
    <p>Characterized by an extremely fine drink, strong body, excellent aroma and sweetness...</p>
    <div class="product-actions"><span class="btn-small btn-shop">Shop Now</span><span class="btn-small btn-cart"><svg width="11" height="10" viewBox="0 0 16 14" aria-hidden="true"><path d="M0 1h3l2 8h8l2-6H4.5Z" fill="#fff"/><circle cx="6" cy="12" r="1.6" fill="#fff"/><circle cx="12" cy="12" r="1.6" fill="#fff"/></svg>Add to Cart</span></div>
  </article>
</div>

<section class="brew">
  <div class="brew-photo" role="img" aria-label="Cup of coffee on a bed of coffee beans, green tinted"></div>
  <div class="brew-inner">
    <h2 class="heading">BREW COFFEE</h2>
    <p>Sed ut perspiciatis unde omnis iste natus error sit voluptatem accusantium doloremque laudantium, totam rem aperiam, eaque ipsa quae ab illo inventore veritatis et quasi architecto beatae vitae dicta sunt explicabo. Nemo enim ipsam voluptatem quia voluptas sit aspernatur aut odit aut fugit, sed quia consequuntur magni dolores eos qui ratione voluptatem sequi nesciunt.</p>
    <p>similique sunt in culpa qui officia deserunt mollitia animi, id est laborum et dolorum fuga. Et harum quidem rerum facilis est et expedita distinctio.</p>
  </div>
</section>

<section class="about">
  <div class="about-photo" role="img" aria-label="Faded top view of a white cup of frothy coffee on a pale wooden table"></div>
  <div class="about-inner">
    <h2 class="heading"><em>OUR</em> PRODUCTS</h2>
    <p>Ut enim ad minima veniam, quis nostrum exercitationem ullam corporis suscipit laboriosam, nisi ut aliquid ex ea commodi consequatur? Quis autem vel eum iure reprehenderit qui in ea voluptate velit esse quam nihil molestiae consequatur.</p>
    <p>Et harum quidem rerum facilis est et expedita distinctio. Nam libero tempore, cum soluta nobis est eligendi optio cumque nihil impedit quo minus.</p>
    <span class="btn-more">Read More Info <svg width="8" height="12" viewBox="0 0 8 12" aria-hidden="true"><path d="M1.5 1l5 5-5 5" fill="none" stroke="#fff" stroke-width="1.6"/></svg></span>
  </div>
</section>

<section class="history">
  <div class="history-photo" role="img" aria-label="Cup of coffee beans on a sack with scattered beans, green tinted"></div>
  <div class="history-inner">
    <h2 class="heading">HISTORY OF THE COMPANY WITH COFFEE</h2>
    <p class="lead">We sell cold brew coffee served in a keg tap.</p>
    <p class="body">At vero eos et accusamus et iusto odio dignissimos ducimus qui blanditiis praesentium voluptatum deleniti atque corrupti quos dolores et quas molestias excepturi.</p>
    <span class="btn-more">Read More Info <svg width="8" height="12" viewBox="0 0 8 12" aria-hidden="true"><path d="M1.5 1l5 5-5 5" fill="none" stroke="#fff" stroke-width="1.6"/></svg></span>
  </div>
</section>

<footer class="site-footer">
  <div class="footer-col col-contact">
    <h4>CONTACT US</h4>
    <p style="margin-top:14px">contact us here.</p>
    <p>we are located in Ferncastle Coldbrew in England.</p>
    <p>If you are a cold brew coffee served like us,</p>
    <p>send us your message!</p>
    <p>We will be pleased to help you.</p>
  </div>
  <div class="divider-v" style="left:456px"></div>
  <div class="footer-col col-touch">
    <h4>GET IN TOUCH</h4>
    <div class="contact-form">
      <div class="field-row"><div class="field">Your Name</div><div class="field">Your Email</div></div>
      <div class="field field-area">Your Message</div>
      <div class="btn-send">SEND</div>
    </div>
  </div>
  <div class="divider-v" style="left:888px"></div>
  <div class="footer-col col-follow">
    <h4>FOLLLOW US</h4>
    <p>Please connect with us on</p>
    <div class="social"><span class="s1"></span><span class="s2"></span><span class="s3"></span><span class="s4"></span></div>
  </div>
  <div class="footer-bottom"><span>© 2016 Company Name &nbsp;All right reserved &nbsp;Term of Use</span><span class="code">C16</span></div>
</footer>

</body>
</html>
```